Geschäftspapiere für Jobwebseite
Zielgruppe
Hier finden sie alle Informationen zu unserem Unternehmen:
https://www.sauberwerk-stelle.com
Aufgabenstellung
Gerne von den Farben angelehnt an die Website ein modernes Briefpapier gestalten.

```html
<!DOCTYPE html>
<html lang="de">
<head>
<meta charset="utf-8">
<title>Briefpapier – Sauberwerk-Stelle</title>
<link rel="stylesheet" href="https://fonts.googleapis.com/css2?family=Open+Sans:wght@400;600;700&family=Fira+Sans:wght@400&display=swap">
<style>
  :root {
    --bg: #ebebeb;
    --paper: #ffffff;
    --green: #2c8c47;
    --green-text: #1f8a3b;
    --ink: #3d3d3d;
    --logo-grey: #555555;
    --sign: #d9dcef;
  }
  * { margin: 0; padding: 0; box-sizing: border-box; }
  html, body { width: 1200px; height: 864px; overflow: hidden; background: var(--bg); }
  body { position: relative; font-family: "Open Sans", Verdana, sans-serif; color: var(--ink); }

  .view-label {
    position: absolute; font-family: "Fira Sans", sans-serif;
    font-size: 15px; color: #222; top: 68px;
  }
  .view-label.folded { left: 106px; }
  .view-label.open { left: 630px; top: 67px; }

  .sheet {
    position: absolute; background: var(--paper);
    box-shadow: 5px 6px 8px rgba(0,0,0,0.22);
  }
  .sheet.folded { left: 106px; top: 95px; width: 484px; height: 242px; }
  .sheet.open { left: 630px; top: 96px; width: 484px; height: 684px; }

  .frame {
    position: absolute; left: 0; top: 0; width: 100%; height: 241px;
    border: 7px solid var(--green); border-bottom: none;
  }
  .sheet.folded .frame { height: 242px; }

  .brand {
    position: absolute; top: 26px; left: 0; width: 100%;
    text-align: center; font-weight: 700; font-size: 15.5px;
    letter-spacing: 0.2px; color: var(--logo-grey);
  }
  .brand-dot {
    display: block; width: 9px; height: 9px; border-radius: 50%;
    background: var(--green); margin: 4px auto 0;
  }

  .sender-line {
    position: absolute; left: 58px; top: 122px;
    font-size: 5.2px; color: #555;
  }
  .sender-line b { color: var(--green-text); font-weight: 700; }

  .recipient {
    position: absolute; left: 58px; top: 136px;
    font-size: 7.4px; line-height: 10.6px;
  }

  .subject {
    position: absolute; left: 58px; top: 217px;
    font-size: 9.8px; font-weight: 700; color: var(--green-text); letter-spacing: 0.1px;
  }

  .fold-mark {
    position: absolute; left: 0; width: 7px; height: 1px; background: var(--green);
  }

  .letter-body {
    position: absolute; left: 58px; top: 257px; width: 300px;
    font-size: 7.3px; line-height: 9.75px;
  }
  .letter-body p { margin-bottom: 9.75px; }
  .letter-body .salutation { margin-bottom: 19.5px; }

  .signature {
    position: absolute; left: 58px; top: 581px; width: 100px; height: 24px;
    background: var(--sign); border-radius: 2px;
  }
  .signer { position: absolute; left: 58px; top: 607px; font-size: 7.4px; }

  .imprint {
    position: absolute; left: 376px; top: 541px; width: 100px;
    font-size: 5.2px; line-height: 9px; color: #444;
  }
  .imprint p { margin-bottom: 8.8px; }
  .imprint .imprint-name { font-weight: 700; font-size: 5.6px; color: var(--ink); }

  .footer-bar {
    position: absolute; left: 376px; bottom: 0; width: 79px; height: 7px; background: var(--green);
  }
</style>
</head>
<body>

  <div class="view-label folded">Gefalzter Brief</div>
  <div class="view-label open">Geöffneter Brief</div>

  <section class="sheet folded">
    <div class="frame"></div>
    <div class="brand">SAUBERWERK-STELLE.de<span class="brand-dot"></span></div>
    <div class="sender-line"><b>SAUBERWERK-STELLE.DE</b> | Gewerbering Nord 7 | 77815 Bühl</div>
    <div class="recipient">Firma: Musterfirma<br>Herr Maximilian Mustermann<br>Musterstraße 11<br>12345 Musterstadt</div>
    <div class="subject">HIER STEHT DER BETREFF</div>
  </section>

  <section class="sheet open">
    <div class="frame"></div>
    <div class="brand">SAUBERWERK-STELLE.de<span class="brand-dot"></span></div>
    <div class="sender-line"><b>SAUBERWERK-STELLE.DE</b> | Gewerbering Nord 7 | 77815 Bühl</div>
    <div class="recipient">Firma: Musterfirma<br>Herr Maximilian Mustermann<br>Musterstraße 11<br>12345 Musterstadt</div>
    <div class="subject">HIER STEHT DER BETREFF</div>

    <div class="fold-mark" style="top:342px"></div>
    <div class="fold-mark" style="top:484px"></div>

    <div class="letter-body">
      <p class="salutation">Sehr geehrter Herr Mustermann,</p>
      <p>Ferem sit, omniendaecte doluptature mo cuptatio. Ebitati ssumqui coria poreici destrum, vidusap elibus qui ipideli tatecabo. Et remporporio di quo ommolup taessit, ius non esequibus et volupiditio optatur ereicat laut et et quae ium int ma sum cori omnimin recus, ent molupti orrores truptassin eos a cor sa sus dolupta sitist laut que plignat.<br>Axim exeribus. Pudit arum ium ipiet in ni od mos ent liciam quunt aborporem verferr uptasim ra de int quunt a inimin et il mi, eaque volo bla volo bea qui ius, sum volo Ibus, acepernatem aut explabo rporupta pa qui consediam atus.</p>
      <p>Aximporporum et dolore conecerferia venimet verae sum nobist asintorest, eosant alique volut qui te nullo eum que velitatatis iumque mint ut volupta tquiatemodi dolless itature, et laccuptae pa invelis sequunt, velique abo. Obis sus et officipsamus premquidi blabo. Dollore rnatend untiatu reperion consequam faccaborit faciates sitatenet harunt invenim di sumque.</p>
      <p>Pore oditam identitiis dit estrunt officta tecust pro maionsequis del mos aut quiatur? Icillab ipsapie nihilluptas mo et que sitatiis dolupta quament laborro cuptae. Namus, utendunt. Pictat. Otae nimet faccatur? Erumqui at occum ratquia nos viti con reiunt volorro ommodit, nusam ratiasr itatet pa quistionsed explitem. Nam inis essinve litatib usdandit miliaspedi aces utatem facia volesci alit evel iuntis unt ab ilit autem quam archilluptae</p>
      <p>Sit laut qui tem rerum as reperae prorempedi neces et acculparum fugiae denetur, torernam verepti issinullenis arum re dolessi sum rerum ra di que vel minciam duntio. Aborios molutae praest, corit quiaerci sus andigente sincius si occum fugiae reperibus delicab is sunt magnam is vento to blandiscia quo dolorro vitasped evelest, suntemp oreictor a porepudaeri que conem aut mint alitam si quae volorro rerferia volorepeliti ad ma voluptat acest estrupta si voloriscid millatatae re, offictis aperor maio. Ut liquam erum eum dunt offici dolenih ilibus, id erro et volupta volectent que pla sitis exped maio. Nam sitatur sit qui comnima ximpore consect ibeatatum aut in nulparc hilite nonsequia autemquat.</p>
      <p>Mit freundlichen Grüßen</p>
    </div>

    <div class="signature" role="img" aria-label="Handschriftliche Unterschrift"></div>
    <div class="signer">Max Mustermann</div>

    <aside class="imprint">
      <p><span class="imprint-name">SAUBERWERK-STELLE.de</span><br>Gewerbering Nord 7<br>77815 Bühl</p>
      <p><b>M</b>&nbsp; info@sauberwerk-stelle.de<br><b>T</b>&nbsp; 07223 415 209 3</p>
      <p>Inhaber<br>Herr Jonas Wendler</p>
      <p>Amtsgericht Mannheim<br>HRB xxxx<br>USt-IdNr. DExxxxxxx</p>
    </aside>

    <div class="footer-bar"></div>
  </section>

</body>
</html>
```